New lease of life for a tired Country Pub menu, QLD

I need to refresh my menus with updated prices. The menus need to be A4 (the menus are laminated and handed out over the bar. I'd like to include our logo. I will upload our existing menus as well as the new prices. The design should be humble yet stylish if that's ok, please

Target Market(s)

Locals, travellers and workers

Industry/Entity Type

Hospitality, Quintessential Country pub

Font styles to use
Sans Serif

Colors

Designer to choose colors to be used in the design.

Requirements
Must have
• as we run different menus on different nights
Nice to have
• our logo

```html
<!DOCTYPE html>
<html lang="en">
<head>
<meta charset="utf-8">
<title>Hotel Barlow – Dinner Menu</title>
<link rel="stylesheet" href="https://fonts.googleapis.com/css2?family=Poppins:wght@300;400;500;600;700&display=swap">
<style>
:root{
  --ink:#1c1a19;
  --cream:#cbc1a8;
  --paper:#ffffff;
}
*{box-sizing:border-box;margin:0;padding:0}
html,body{width:1200px;height:830px;overflow:hidden;background:var(--paper)}
body{position:relative;font-family:"Poppins",sans-serif;color:var(--cream)}
.page{position:absolute;background:var(--ink);height:830px}
.page--food{left:0;top:7px;width:582px}
.page--extras{left:615px;top:0;width:585px}
.frame{position:absolute;border:4px solid var(--cream)}
.abs{position:absolute}
.venue{position:absolute;width:200px;text-align:center;font-weight:700;font-size:19px;line-height:20px;letter-spacing:.5px}
.title{position:absolute;width:480px;text-align:center;font-weight:400;font-size:57px;line-height:60px;letter-spacing:1px;color:transparent;-webkit-text-stroke:1.6px var(--cream)}
.heading{position:absolute;font-weight:600;font-size:29px;line-height:34px;white-space:nowrap}
.heading--center{text-align:center;width:360px}
.row{position:absolute;display:flex;align-items:flex-end;font-weight:600;font-size:11.5px;line-height:14px;white-space:nowrap;text-transform:uppercase}
.row--dish{font-weight:500;font-size:13.5px;line-height:16px;text-transform:none}
.dots{flex:1;height:4px;margin:0 3px 3px;background:radial-gradient(circle,var(--cream) 1px,transparent 1.3px) 0 50%/6px 4px repeat-x}
.row--dish .dots{background-size:4.5px 4px}
.dots--short{flex:0 0 16px}
.label{position:absolute;font-weight:600;font-size:11.5px;line-height:14px;text-transform:uppercase;white-space:nowrap}
.icon{position:absolute;background:var(--cream);border-radius:6px;opacity:.9}
.note{position:absolute;width:240px;text-align:center;font-weight:300;font-size:16px;line-height:20px}
.drink-title{position:absolute;font-weight:700;font-size:13.5px;line-height:16px;white-space:nowrap}
.drink-list{position:absolute;list-style:none;font-weight:500;font-size:10.5px;line-height:15.6px;white-space:nowrap}
</style>
</head>
<body>

<section class="page page--food">
  <div class="frame" style="left:35px;top:36px;width:512px;height:752px"></div>
  <div class="venue" style="left:191px;top:82px">HOTEL<br>BARLOW</div>
  <h1 class="title" style="left:51px;top:163px">DINNER MENU</h1>

  <h2 class="heading heading--center" style="left:111px;top:232px">Garlic Bread Starters</h2>
  <div class="row" style="left:70px;top:286px;width:186px"><span>Regular</span><i class="dots"></i><span>$10.50</span></div>
  <div class="row" style="left:70px;top:307px;width:186px"><span>Cheesy Garlic</span><i class="dots"></i><span>$12.00</span></div>
  <div class="row" style="left:326px;top:286px;width:186px"><span>Cheesy Sweet Chili</span><i class="dots"></i><span>$12.50</span></div>
  <div class="row" style="left:326px;top:307px;width:186px"><span>Loaded</span><i class="dots"></i><span>$15.00</span></div>

  <h2 class="heading heading--center" style="left:111px;top:335px">Main Course</h2>

  <div class="icon" role="img" aria-label="Beef icon" style="left:60px;top:401px;width:40px;height:28px"></div>
  <div class="row row--dish" style="left:115px;top:384px;width:395px"><span>T-Bone Steak</span><i class="dots"></i><span>$41.99</span></div>
  <div class="row row--dish" style="left:115px;top:401px;width:395px"><span>Rump Steak</span><i class="dots"></i><span>$40.99</span></div>
  <div class="row row--dish" style="left:115px;top:419px;width:395px"><span>Crumbed Steak</span><i class="dots"></i><span>$28.99</span></div>

  <div class="icon" role="img" aria-label="Lamb icon" style="left:60px;top:468px;width:40px;height:30px"></div>
  <div class="row row--dish" style="left:115px;top:455px;width:395px"><span>Lamb Rosemary Filo</span><i class="dots"></i><span>$24.99</span></div>
  <div class="row row--dish" style="left:115px;top:472px;width:395px"><span>Lamb Shank and Mash</span><i class="dots"></i><span>$32.00</span></div>
  <div class="row row--dish" style="left:115px;top:490px;width:395px"><span>Lamb Loin Chops</span><i class="dots"></i><span>$35.00</span></div>

  <div class="icon" role="img" aria-label="Pork icon" style="left:60px;top:525px;width:40px;height:22px"></div>
  <div class="row row--dish" style="left:115px;top:525px;width:395px"><span>Pork Chop(s)</span><i class="dots"></i><span>$29.00 (1)</span><i class="dots dots--short"></i><span>$32.99 (2)</span></div>

  <div class="icon" role="img" aria-label="Chicken icon" style="left:67px;top:571px;width:26px;height:27px"></div>
  <div class="row row--dish" style="left:115px;top:567px;width:395px"><span>Chicken and Mushroom Filo</span><i class="dots"></i><span>$24.99</span></div>
  <div class="row row--dish" style="left:115px;top:584px;width:395px"><span>Crumbed Chicken Thigh</span><i class="dots"></i><span>$27.99</span></div>

  <div class="icon" role="img" aria-label="Sausage and potato icon" style="left:61px;top:622px;width:38px;height:26px"></div>
  <div class="row row--dish" style="left:115px;top:620px;width:395px"><span>Bangers and Mash</span><i class="dots"></i><span>$23.00</span></div>
  <div class="row row--dish" style="left:115px;top:637px;width:395px"><span>Rissoles and Mash</span><i class="dots"></i><span>$23.00</span></div>

  <div class="icon" role="img" aria-label="Carrot icon" style="left:66px;top:667px;width:28px;height:28px"></div>
  <div class="row row--dish" style="left:115px;top:673px;width:395px"><span>Roasted Veggie Scroll</span><i class="dots"></i><span>$24.99</span></div>

  <div class="icon" role="img" aria-label="Fish icon" style="left:65px;top:734px;width:30px;height:17px"></div>
  <div class="row row--dish" style="left:115px;top:708px;width:395px"><span>Beer Battered Flathead (Main)</span><i class="dots"></i><span>$27.99</span></div>
  <div class="row row--dish" style="left:115px;top:725px;width:395px"><span>Barramundi Panko</span><i class="dots"></i><span>$27.99</span></div>
  <div class="row row--dish" style="left:115px;top:743px;width:395px"><span>Calamari Panko Crumbed</span><i class="dots"></i><span>$27.99</span></div>
  <div class="row row--dish" style="left:115px;top:761px;width:395px"><span>Seafood Basket</span><i class="dots"></i><span>$27.99</span></div>
</section>

<section class="page page--extras">
  <div class="frame" style="left:35px;top:43px;width:512px;height:752px"></div>
  <div class="venue" style="left:191px;top:89px">HOTEL<br>BARLOW</div>
  <h1 class="title" style="left:51px;top:170px">DINNER MENU</h1>

  <div class="icon" role="img" aria-label="Salad bowl icon" style="left:105px;top:240px;width:31px;height:30px"></div>
  <h2 class="heading" style="left:142px;top:239px">Sides</h2>
  <div class="icon" role="img" aria-label="Sauce bowl icon" style="left:347px;top:240px;width:31px;height:30px"></div>
  <h2 class="heading" style="left:383px;top:239px">Sauces</h2>

  <div class="row" style="left:52px;top:293px;width:214px"><span>Small Bowl of Chips</span><i class="dots"></i><span>$9.50</span></div>
  <div class="row" style="left:52px;top:316px;width:214px"><span>Large Bowl of Chips</span><i class="dots"></i><span>$12.50</span></div>
  <div class="row" style="left:52px;top:340px;width:214px"><span>Mash Potatoes</span><i class="dots"></i><span>$4.99</span></div>
  <div class="row" style="left:52px;top:363px;width:214px"><span>Side Salad</span><i class="dots"></i><span>$10.00</span></div>

  <div class="row" style="left:308px;top:293px;width:213px"><span>Diane Sauce</span><i class="dots"></i><span>$9.50</span></div>
  <div class="row" style="left:308px;top:316px;width:213px"><span>Gravy</span><i class="dots"></i><span>$12.50</span></div>
  <div class="row" style="left:308px;top:340px;width:213px"><span>Mushroom Sauce</span><i class="dots"></i><span>$4.99</span></div>
  <div class="row" style="left:308px;top:363px;width:213px"><span>Pepper Sauce</span><i class="dots"></i><span>$10.00</span></div>
  <div class="row" style="left:308px;top:387px;width:213px"><span>Aioli</span><i class="dots"></i><span>$9.50</span></div>
  <div class="row" style="left:308px;top:410px;width:213px"><span>Mayonnaise</span><i class="dots"></i><span>$12.50</span></div>
  <div class="row" style="left:308px;top:433px;width:213px"><span>Tartar</span><i class="dots"></i><span>$4.99</span></div>

  <div class="icon" role="img" aria-label="Kids icon" style="left:60px;top:423px;width:50px;height:24px;border-radius:12px"></div>
  <h2 class="heading" style="left:114px;top:418px">Kids Menu</h2>

  <div class="label" style="left:52px;top:472px">Beer Battered</div>
  <div class="row" style="left:63px;top:485px;width:203px"><span>Flat Bread (Kids)</span><i class="dots"></i><span>$9.50</span></div>
  <div class="row" style="left:52px;top:509px;width:214px"><span>Nuggets &amp; Chips</span><i class="dots"></i><span>$12.50</span></div>
  <div class="row" style="left:52px;top:533px;width:214px"><span>Calamari &amp; Chips</span><i class="dots"></i><span>$4.99</span></div>
  <div class="label" style="left:52px;top:556px">Hawaiian Pizza</div>
  <div class="row" style="left:63px;top:572px;width:203px"><span>And Chips</span><i class="dots"></i><span>$10.00</span></div>

  <div class="icon" role="img" aria-label="Cake slice icon" style="left:332px;top:493px;width:40px;height:30px"></div>
  <h2 class="heading" style="left:378px;top:490px">Desserts</h2>
  <p class="note" style="left:298px;top:547px">Ask your server about today’s delicious selection</p>

  <h2 class="heading heading--center" style="left:119px;top:611px">Beverages</h2>

  <div class="icon" role="img" aria-label="Soft drink icon" style="left:51px;top:661px;width:17px;height:26px"></div>
  <h3 class="drink-title" style="left:79px;top:659px">SOFT DRINKS</h3>
  <ul class="drink-list" style="left:79px;top:676px"><li>Cola, Diet Cola,</li><li>Lemonade, Root Beer,</li><li>Orange Soda</li></ul>

  <div class="icon" role="img" aria-label="Juice glass icon" style="left:189px;top:661px;width:13px;height:23px"></div>
  <h3 class="drink-title" style="left:212px;top:659px">JUICES</h3>
  <ul class="drink-list" style="left:212px;top:676px"><li>Orange</li><li>Apples</li><li>Cranberry</li></ul>

  <div class="icon" role="img" aria-label="Coffee cup icon" style="left:277px;top:662px;width:23px;height:21px"></div>
  <h3 class="drink-title" style="left:309px;top:659px">Coffee &amp; Tea</h3>
  <ul class="drink-list" style="left:309px;top:676px"><li>Regular</li><li>Decaf</li><li>Orange Pekoe</li><li>Earl Grey</li><li>English Breakfast</li></ul>

  <div class="icon" role="img" aria-label="Beer mug icon" style="left:412px;top:661px;width:24px;height:24px"></div>
  <h3 class="drink-title" style="left:444px;top:659px">BEER &amp; WINE</h3>
  <ul class="drink-list" style="left:444px;top:676px"><li>Gold Lager</li><li>Northern Pale</li><li>Ridge Ale</li><li>House Red</li><li>House White</li></ul>
</section>

</body>
</html>
```